Multifamily Investment Strategies

I need a pamphlet or booklet for multifamily commercial real estate investment.

The specific investment vehicle is affordable multifamily apartments. I have uploaded a 5 page pdf detailing my investment strategy.

The target audience for this pamphlet are investors, commercial brokers, and commercial bankers.

I am looking for modern, clean design that is striking and professional but also eye catching.
Updates

I made a few changes to the brief and also corrected two errors.

Target Market(s)

Commercial Real Estate Investors, Brokers, and Bankers

Industry/Entity Type

Real Estate

Font styles to use
Serif

Colors

Designer to choose colors to be used in the design.

Requirements
Must have
• Graphics of or related to apartment buildings.
• My headshot seen on the last page of the pdf
Nice to have
• Imagery related to investment and profits.
Should not have
• The image of an apartment building on the first page of the pdf is just an example. Please don’t use this image.

```html
<!DOCTYPE html>
<html lang="en">
<head>
<meta charset="utf-8">
<title>Multifamily Cashflow Investment Strategy</title>
<link href="https://fonts.googleapis.com/css2?family=Saira+Extra+Condensed:wght@300;600&family=Roboto+Condensed:wght@400;700&display=swap" rel="stylesheet">
<style>
:root{
  --blue:#1496e0;
  --navy:#134a86;
  --ink:#3a3a3a;
  --tag-dark:#2b2b2b;
  --accent:#1a8ad4;
  --head:#2a6aa8;
  --grey-head:#7a7a7a;
  --paper:#ffffff;
  --mist:#f1f1f1;
  --panel:#e4e4e4;
  --box:#ececec;
}
*{margin:0;padding:0;box-sizing:border-box}
html,body{width:1200px;height:777px;overflow:hidden;background:var(--paper)}
body{font-family:"Roboto Condensed",Arial,sans-serif;color:var(--ink);position:relative}
.spread{position:absolute;inset:0;width:1200px;height:777px}
.page-left{position:absolute;left:0;top:0;width:600px;height:720px;background:linear-gradient(90deg,#fff 70%,#eee 100%)}
.page-right{position:absolute;left:600px;top:0;width:600px;height:720px;background:linear-gradient(90deg,#e6e6e6 0%,var(--mist) 8%,#fafafa 100%)}
.hero-band{position:absolute;left:0;top:0;width:600px;height:216px;background:linear-gradient(90deg,#1da0e6 0%,#1592da 60%,#0a6fbf 100%)}
.hero-steps{position:absolute;left:0;top:0}
.display{position:absolute;overflow:visible;font-family:"Saira Extra Condensed",sans-serif}
.display text{font-family:"Saira Extra Condensed",sans-serif}
.t-light{font-weight:300}
.t-bold{font-weight:600}
.abs{position:absolute}
.key{color:var(--accent);font-weight:700}
.look{left:53px;top:278px;font-size:13.5px;font-weight:700;color:var(--accent)}
.value-add{left:173px;top:237px;width:360px;font-size:10px;line-height:13px}
.criteria{left:53px;top:307px;width:183px}
.criterion{font-size:9.8px;line-height:14.7px;text-align:justify;margin-bottom:9px}
.tag{display:inline-block;font-weight:700;color:#fff;background:var(--accent);padding:0 9px 0 0;margin-right:4px;line-height:13px;clip-path:polygon(0 0,92% 0,100% 100%,0 100%)}
.tag b{display:inline-block;background:var(--tag-dark);padding:0 3px;margin-right:3px}
.detail{left:265px;top:304px;width:285px}
.callout{background:var(--box);border-radius:6px;padding:4px 4px 3px 7px;margin-bottom:7px;font-size:9.8px;line-height:14.7px}
.detail p{font-size:9.8px;line-height:14.7px;text-align:justify;margin-bottom:9px}
.bullets{list-style:none;font-size:9.6px;line-height:13px}
.bullets li{padding-left:9px;position:relative}
.bullets li::before{content:"•";position:absolute;left:0;color:#999}
.bullets .sub li{padding-left:18px}
.bullets .sub li::before{left:9px}
.panel{position:absolute;left:600px;top:348px;width:600px;height:372px;background:var(--panel)}
.illustration{position:absolute;left:600px;top:470px;width:253px;height:250px;background:linear-gradient(160deg,rgba(228,228,228,0) 0%,#e2e5ea 35%,#f4b45a 62%,#9ac46a 88%,#6aa84a 100%);opacity:.85}
.strategy{position:absolute;left:862px;width:300px}
.strategy h3{font-size:10.5px;font-weight:700;color:var(--head);line-height:14px}
.strategy h3 .n{font-family:"Saira Extra Condensed",sans-serif;font-weight:600;font-size:22px;line-height:0;vertical-align:-2px}
.strategy ul{margin-top:3px;font-size:8.8px;line-height:11.5px}
.footer{position:absolute;left:0;top:720px;width:1200px;height:57px;background:linear-gradient(90deg,var(--blue) 0%,#1a9be3 49%,#0c7fcf 50%,var(--blue) 100%)}
.footer .rule{position:absolute;left:0;top:27px;width:44px;height:6px;background:#fff}
.footer .doc{position:absolute;left:51px;top:22px;font-size:11px;color:#fff;letter-spacing:.3px}
.footer .sign{position:absolute;right:28px;top:22px;font-size:10px;color:#fff}
</style>
</head>
<body>
<div class="spread">
  <div class="page-left"></div>
  <div class="page-right"></div>

  <div class="hero-band"></div>
  <svg class="hero-steps" width="200" height="216" viewBox="0 0 200 216">
    <polygon points="0,72 72,72 72,144 143,144 143,216 0,216" fill="#fff"/>
    <polygon points="72,72 105,144 72,144" fill="#1565c0"/>
    <polygon points="143,144 176,216 143,216" fill="#1565c0"/>
  </svg>

  <svg class="display" style="left:376px;top:60px" width="140" height="110" viewBox="0 0 140 110">
    <title>3 Steps for Success</title>
    <text class="t-light" x="0" y="64" font-size="78" fill="var(--navy)" textLength="140" lengthAdjust="spacingAndGlyphs">3 STEPS</text>
    <text class="t-light" x="0" y="104" font-size="45" fill="#fff" textLength="140" lengthAdjust="spacingAndGlyphs">FOR SUCCESS</text>
  </svg>

  <svg class="display" style="left:52px;top:230px" width="104" height="32" viewBox="0 0 104 32">
    <text class="t-bold" x="0" y="27" font-size="34" fill="var(--head)" textLength="102" lengthAdjust="spacingAndGlyphs">1. Buy Right:</text>
  </svg>
  <div class="abs value-add">
    <div class="key">• Value Add - Key questions when considering a property:</div>
    <div>• Who owns it? &nbsp; • How long have they owned it? &nbsp;• Why are they selling it?</div>
  </div>
  <div class="abs look">What to look for:</div>

  <div class="abs criteria">
    <p class="criterion"><span class="tag"><b>A.</b>Poor management</span> typically by individual owners, families, or out of state management.</p>
    <p class="criterion"><span class="tag"><b>B.</b>Under market rents</span> rates significantly below comparable prices in the area.</p>
    <p class="criterion"><span class="tag"><b>C.</b>Deferred maintenance</span> this can be a sign of a motivated or “burned-out” seller. Light exterior and interior upgrades, e.g., paint, landscaping, carpet replacement, fixture and appliance upgrades, will have a significant impact.</p>
    <p class="criterion"><span class="tag"><b>D.</b>High vacancy</span> often due to poor marketing.</p>
    <p class="criterion"><span class="tag"><b>E.</b>Motivated sellers</span> allows for negotiation a lower price. Common motivators include divorce, bankruptcy, retirement, inherited properties, new investment opportunity, burnout, etc.</p>
    <p class="criterion"><span class="tag"><b>F.</b>Owner paid utilities</span> allows for significant upside in income through implementing Ratio Utility Business System (RUBS)</p>
  </div>

  <div class="abs detail">
    <div class="callout">By tackling these issues, we will successfully reposition the property, which will significantly increase the income. As a result, <strong>the value of the property</strong> will also increase.</div>
    <p><span class="key">Property Class</span> - B and C class properties in A and B neighborhoods - Prefer 1980’s or newer.</p>
    <p>These properties tend to house blue collar workers; don’t compete with new(er) construction; and don’t share the same challenges as C and D properties in C and D neighborhoods, which can encounter issues with crime, major disrepair, and increased vulnerability to economic downturns.</p>
    <p><span class="key">Market Analysis</span> - Target emerging markets with population and job growth; low to median cost of housing which allows rent growth (e.g., Columbus, Oklahoma, Atlanta, Dallas, Phoenix); median income of ~$35k/ yr; and landlord and business friendly rules and regulations (e.g., Ohio, Texas, Florida, Oklahoma, Colorado).</p>
    <p><span class="key">Scale</span> - 60+ units to support effective, third-party professional management. Additionally, targeting 60+units will increase the likelihood of stability by creating a buffer against tenant turnover and other unplanned expenses.</p>
    <p><span class="key">Cash flow</span> - The property must generate cash flow from day one, before value add strategies are deployed.</p>
    <p style="text-align:left">Buy on <strong>actual numbers</strong> instead of on pro forma analysis, which project or estimate financial return</p>
  </div>

  <svg class="display" style="left:646px;top:56px" width="142" height="30" viewBox="0 0 142 30">
    <text class="t-bold" x="0" y="25" font-size="32" fill="var(--head)" textLength="140" lengthAdjust="spacingAndGlyphs">2. Finance Right:</text>
  </svg>
  <ul class="abs bullets" style="left:646px;top:92px;width:510px">
    <li><strong>Longterm debt</strong> - with long terms and amortization periods.</li>
    <li><strong>Non-recourse</strong> if possible. e.g ., Union Home Finance, Keystone Mortgage Co., Local/Regional lenders. There is an extremely low foreclosure rate for agency underwritten properties (1%-2%).</li>
    <li><strong>No prepayment penalty.</strong></li>
    <li><strong>No due on sale clause.</strong></li>
  </ul>

  <svg class="display" style="left:646px;top:176px" width="144" height="30" viewBox="0 0 144 30">
    <text class="t-bold" x="0" y="25" font-size="32" fill="var(--head)" textLength="142" lengthAdjust="spacingAndGlyphs">3. Manage Right:</text>
  </svg>
  <ul class="abs bullets" style="left:646px;top:211px;width:510px">
    <li><strong>Third-Party Management with experience in this specific class of multifamily real estate.</strong>
      <ul class="sub bullets">
        <li>Sizable but not too large that our property gets lost.</li>
        <li>Only in property management, not acquisition or development so that there is no conflict of interest.</li>
      </ul></li>
    <li><strong>Use of Sole Purpose Entity Structures, e.g., LLC’s for asset protection.</strong></li>
    <li><strong>Optimization through use of systems.</strong></li>
    <li><strong>Tenant satisfaction</strong> - Ensure great customer service to the tenant, e.g., 24 hour response to maintenance requests, cleanliness, and security. Happy tenants who feel heard and cared for, don’t leave, which limits tenant turnover, and lowers expenses.</li>
    <li><strong>Increase the “curb appeal”</strong> - Freshened exterior with modern paint schemes, landscaping, and new signage. Rebranding with a name change, webpage, etc.</li>
  </ul>

  <div class="panel"></div>
  <div class="illustration" role="img" aria-label="Illustration of a rising red arrow over stacked gold coins and a row of colourful apartment buildings and trees"></div>

  <svg class="display" style="left:646px;top:385px" width="152" height="130" viewBox="0 0 152 130">
    <title>6 Strategies for Increasing Income</title>
    <text class="t-light" x="0" y="35" font-size="40" fill="var(--grey-head)" textLength="150" lengthAdjust="spacingAndGlyphs">6 STRATEGIES FOR</text>
    <text class="t-light" x="0" y="79" font-size="62" fill="var(--accent)" textLength="150" lengthAdjust="spacingAndGlyphs">INCREASING</text>
    <text class="t-light" x="0" y="125" font-size="62" fill="var(--accent)" textLength="94" lengthAdjust="spacingAndGlyphs">INCOME</text>
  </svg>

  <div class="strategy" style="top:392px">
    <h3><span class="n">1</span>. Fill vacant units at market rate</h3>
    <ul class="bullets"><li>After light renovation (&lt; $1,000 per unit) - modern, two-tone paint schemes (white trim, taupe / light grey walls); vinyl wood plank flooring to replace carpet; cleaning of existing carpet.</li></ul>
  </div>
  <div class="strategy" style="top:475px">
    <h3><span class="n">2</span>. Employ RUBS, where applicable</h3>
    <ul class="bullets"><li>Pre-calculated formula for billing back a tenant’s utilities.</li><li>Water, sewer, trash, gas/electric.</li></ul>
  </div>
  <div class="strategy" style="top:534px">
    <h3><span class="n">3</span>. Gradually raise existing tenants to market rate AFTER adding value</h3>
    <ul class="bullets"><li>Improve the exterior “curb appeal” - power washing, landscaping, painting. Inexpensive and effective.</li></ul>
  </div>
  <div class="strategy" style="top:606px">
    <h3><span class="n">4</span>. Fees - Pet fees; deposits; late fees (without exception); move-in fees</h3>
  </div>
  <div class="strategy" style="top:656px">
    <h3><span class="n">5</span>. Laundry machines</h3>
  </div>
  <div class="strategy" style="top:693px">
    <h3><span class="n">6</span>. Lower expenses through renegotiation of contracts</h3>
  </div>

  <footer class="footer">
    <span class="rule"></span>
    <span class="doc">MULTIFAMILY CASHFLOW INVESTMENT STRATEGY</span>
    <span class="sign"><strong>Dana Whitfield</strong> &nbsp;| &nbsp;Real Estate Investor</span>
  </footer>
</div>
</body>
</html>
```